Hydrographic business needs a business card that reaches hunters and off-road enthusiasts

We need a business card for a new hydrographics company catering to customers such as hunters, off-road ATV riders and custom vehicle enthusiasts. A western theme is preferred but professional. Our service should be thought of as upper end graphic design on firearms, off road vehicles, motorcycles, etc... See www.caldorfx.com for ideas on patterns, colors, etc...

Target Market(s)

Hunters, off road enthusiasts, custom car enthusiasts, motorcycle riders...

Industry/Entity Type

Graphic Design

```html
<!DOCTYPE html>
<html lang="en">
<head>
<meta charset="utf-8">
<title>Caldor Hydro Graphics – Business Card</title>
<link rel="stylesheet" href="https://fonts.googleapis.com/css2?family=Roboto+Condensed:wght@400;700&family=Kaushan+Script&display=swap">
<style>
  :root {
    --backdrop: #2e2733;
    --wood-light: #a08a6c;
    --wood-mid: #8a7358;
    --wood-dark: #6f5a42;
    --ink: #ffffff;
    --card-edge: #f2efe9;
  }
  * { box-sizing: border-box; margin: 0; padding: 0; }
  html, body {
    width: 1200px; height: 834px; overflow: hidden;
    background: var(--backdrop);
  }
  .canvas {
    position: relative; width: 1200px; height: 834px;
    display: flex; align-items: center; justify-content: center; gap: 40px;
  }
  .card {
    position: relative; width: 540px; height: 309px;
    border-radius: 4px; overflow: hidden;
    color: var(--ink);
    font-family: "Roboto Condensed", Arial, sans-serif;
    box-shadow: 0 0 0 2px var(--card-edge), 0 14px 30px rgba(0,0,0,.45);
  }
  .card__wood {
    position: absolute; inset: 0;
    background: linear-gradient(160deg, var(--wood-light) 0%, var(--wood-mid) 55%, var(--wood-dark) 100%);
  }
  .card__content { position: absolute; inset: 0; }

  /* Front */
  .front .brand-name {
    position: absolute; left: 0; right: 0; top: 92px;
    text-align: center; font-weight: 700; font-size: 46px; letter-spacing: .5px;
    text-shadow: 0 1px 2px rgba(0,0,0,.35);
  }
  .front .tagline {
    position: absolute; left: 0; right: 0; top: 168px;
    text-align: center; font-size: 19px;
    text-shadow: 0 1px 2px rgba(0,0,0,.35);
  }

  /* Back */
  .back .brand-mark {
    position: absolute; left: 40px; top: 28px;
    display: flex; align-items: center; gap: 10px;
    font-weight: 700; font-size: 26px; line-height: 1.05;
    text-shadow: 0 1px 2px rgba(0,0,0,.35);
  }
  .back .brand-mark__dot {
    width: 18px; height: 18px; border-radius: 50%; background: var(--ink); flex: none;
  }
  .back .tagline {
    position: absolute; left: 40px; top: 112px; width: 190px;
    font-size: 16px; line-height: 1.2;
    text-shadow: 0 1px 2px rgba(0,0,0,.35);
  }
  .back .person {
    position: absolute; right: 28px; top: 28px;
    font-family: "Kaushan Script", cursive; font-size: 28px;
    text-shadow: 0 1px 2px rgba(0,0,0,.35);
  }
  .contact {
    position: absolute; right: 24px; top: 100px;
    list-style: none; font-size: 16px;
  }
  .contact__item {
    display: flex; align-items: center; justify-content: flex-end; gap: 14px;
    min-height: 42px; text-align: right; line-height: 1.2;
    text-shadow: 0 1px 2px rgba(0,0,0,.35);
  }
  .contact__icon { width: 22px; height: 22px; flex: none; fill: var(--ink); }
</style>
</head>
<body>
<main class="canvas">

  <section class="card front" aria-label="Card front">
    <div class="card__wood" role="img" aria-label="Weathered wooden plank texture"></div>
    <div class="card__content">
      <h1 class="brand-name">Caldor Hydro Graphics</h1>
      <p class="tagline">the best and most reliable hydrographics service in East Texas</p>
    </div>
  </section>

  <section class="card back" aria-label="Card back">
    <div class="card__wood" role="img" aria-label="Weathered wooden plank texture"></div>
    <div class="card__content">
      <div class="brand-mark">
        <span class="brand-mark__dot"></span>
        <span>Caldor Hydro<br>Graphics</span>
      </div>
      <p class="tagline">the best and most reliable hydrographics service in East Texas</p>
      <p class="person">Wade Caldor</p>
      <ul class="contact">
        <li class="contact__item">
          <span>512 FM County Road 2210<br>Elm Ridge, TX 75088</span>
          <svg class="contact__icon" viewBox="0 0 24 24" aria-hidden="true"><path d="M12 2a7 7 0 0 0-7 7c0 5 7 13 7 13s7-8 7-13a7 7 0 0 0-7-7zm0 9.5A2.5 2.5 0 1 1 12 6.5a2.5 2.5 0 0 1 0 5z"/></svg>
        </li>
        <li class="contact__item">
          <span>214-555-0187</span>
          <svg class="contact__icon" viewBox="0 0 24 24" aria-hidden="true"><path d="M6.6 10.8a15 15 0 0 0 6.6 6.6l2.2-2.2a1 1 0 0 1 1-.25 11.4 11.4 0 0 0 3.6.57 1 1 0 0 1 1 1V20a1 1 0 0 1-1 1A17 17 0 0 1 3 4a1 1 0 0 1 1-1h3.5a1 1 0 0 1 1 1c0 1.25.2 2.45.57 3.57a1 1 0 0 1-.25 1z"/></svg>
        </li>
        <li class="contact__item">
          <span>wade@caldorfx.com</span>
          <svg class="contact__icon" viewBox="0 0 24 24" aria-hidden="true"><path d="M2 5h20v14H2zm2 2v.4l8 5.2 8-5.2V7zm0 2.8V17h16V9.8l-8 5.2z"/></svg>
        </li>
        <li class="contact__item">
          <span>www.caldorfx.com</span>
          <svg class="contact__icon" viewBox="0 0 24 24" aria-hidden="true"><circle cx="12" cy="12" r="9" fill="none" stroke="#fff" stroke-width="2"/><ellipse cx="12" cy="12" rx="4" ry="9" fill="none" stroke="#fff" stroke-width="1.6"/><path d="M3 12h18M5 7.5h14M5 16.5h14" stroke="#fff" stroke-width="1.4" fill="none"/></svg>
        </li>
      </ul>
    </div>
  </section>

</main>
</body>
</html>
```